Holbrook Legal Group
Project: Stationary for law firm
Stationary for law firm - Law
Stationary for law firm
Use standard fonts
TOMAS VERDELL
Principal Attorney
48210 Pellman Avenue, Suite 415 Woodland Hills, California 90812
legaldesk@brivomail.example
HolbrookLegalGroup.example
dmitrivlaw dmitrivlaw
Kindly note this logo is our old logo design. We have a new logo and files were uploaded.
Please see brief and uploaded files.

```html
<!DOCTYPE html>
<html lang="en">
<head>
<meta charset="utf-8">
<title>Holbrook Legal Group – Business Card</title>
<link href="https://fonts.googleapis.com/css2?family=Cinzel:wght@400;600&family=Montserrat:wght@400;600&display=swap" rel="stylesheet">
<style>
  :root {
    --bg: #d9dadc;
    --card: #ffffff;
    --slate: #56657f;
    --ink: #2f3a52;
    --muted: #6b7489;
    --on-slate: #ffffff;
  }
  * { box-sizing: border-box; margin: 0; padding: 0; }
  html, body { width: 1200px; height: 895px; overflow: hidden; }
  body {
    background: var(--bg);
    font-family: "Montserrat", Arial, sans-serif;
    position: relative;
  }
  .card {
    position: absolute;
    left: 250px;
    width: 700px;
    height: 400px;
    background: var(--card);
    box-shadow: 0 6px 18px rgba(0,0,0,.12);
    overflow: hidden;
  }
  .card--front { top: 27px; }
  .card--back { top: 468px; }

  .accent-band {
    position: absolute;
    right: 0;
    background: var(--slate);
    height: 26px;
  }
  .card--front .accent-band { top: 48px; width: 210px; }
  .card--back .accent-band { top: 140px; width: 200px; }

  .brand { position: absolute; display: flex; align-items: center; gap: 12px; }
  .card--front .brand { left: 250px; top: 100px; }
  .card--back .brand { left: 38px; top: 34px; }
  .brand-square { width: 34px; height: 34px; background: var(--ink); flex: none; }
  .brand-name {
    font-family: "Cinzel", Georgia, serif;
    font-weight: 400;
    font-size: 25px;
    color: var(--ink);
    letter-spacing: .5px;
    line-height: 1;
  }
  .brand-sub {
    font-family: "Cinzel", Georgia, serif;
    font-size: 9.5px;
    color: var(--muted);
    letter-spacing: 1.2px;
    margin-top: 5px;
    line-height: 1.35;
  }

  .person { position: absolute; right: 34px; top: 186px; text-align: right; color: var(--ink); }
  .person-name { font-weight: 600; font-size: 17px; letter-spacing: 1px; }
  .person-title { font-size: 10px; letter-spacing: 1.4px; margin-top: 4px; }

  .contact-cell {
    position: absolute;
    background: var(--slate);
    color: var(--on-slate);
    display: flex;
    flex-direction: column;
    align-items: center;
    justify-content: center;
    gap: 16px;
    font-size: 12px;
    text-align: center;
    line-height: 1.5;
    padding: 0 8px;
  }
  .contact-cell--phone { left: 34px; top: 172px; width: 202px; height: 198px; border-radius: 14px 0 0 14px; }
  .contact-cell--web { left: 240px; top: 172px; width: 202px; height: 198px; border-radius: 0 14px 0 0; font-size: 11px; }
  .contact-cell--address { left: 446px; top: 246px; width: 220px; height: 124px; border-radius: 0 14px 14px 0; gap: 8px; font-size: 11px; line-height: 1.4; }
  .contact-icon { width: 30px; height: 30px; }
  .contact-cell--address .contact-icon { width: 26px; height: 26px; }
</style>
</head>
<body>

<section class="card card--front">
  <div class="accent-band"></div>
  <div class="brand">
    <div class="brand-square"></div>
    <div>
      <div class="brand-name">Holbrook Legal Group</div>
      <div class="brand-sub">Tomas Verdell, Esq<br>Principal | Attorney at Law</div>
    </div>
  </div>
</section>

<section class="card card--back">
  <div class="brand">
    <div class="brand-square"></div>
    <div>
      <div class="brand-name">Holbrook Legal Group</div>
      <div class="brand-sub">Tomas Verdell, Esq<br>Principal | Attorney at Law</div>
    </div>
  </div>
  <div class="accent-band"></div>

  <div class="person">
    <div class="person-name">TOMAS VERDELL</div>
    <div class="person-title">PRINCIPAL ATTORNEY</div>
  </div>

  <div class="contact-cell contact-cell--phone">
    <svg class="contact-icon" viewBox="0 0 24 24" fill="none" stroke="#fff" stroke-width="1.6" stroke-linejoin="round">
      <path d="M3 9c0-3 4-5 9-5s9 2 9 5v1.5h-4V8.5c-1.5-.6-3.2-.9-5-.9s-3.5.3-5 .9v2H3z"/>
      <path d="M6 12h12l2 7H4z"/>
      <circle cx="12" cy="15.5" r="1.8"/>
    </svg>
    <div>(818) 555-0147<br>(818) 555-0148</div>
  </div>

  <div class="contact-cell contact-cell--web">
    <svg class="contact-icon" viewBox="0 0 24 24" fill="none" stroke="#fff" stroke-width="1.5">
      <circle cx="12" cy="12" r="9"/>
      <ellipse cx="12" cy="12" rx="4" ry="9"/>
      <path d="M3 12h18M5 7h14M5 17h14"/>
    </svg>
    <div>legaldesk@brivomail.example<br>HolbrookLegalGroup.example</div>
  </div>

  <div class="contact-cell contact-cell--address">
    <svg class="contact-icon" viewBox="0 0 24 24" fill="none" stroke="#fff" stroke-width="1.6">
      <path d="M12 22s-7-7.5-7-12a7 7 0 0 1 14 0c0 4.5-7 12-7 12z"/>
      <circle cx="12" cy="10" r="2.5"/>
    </svg>
    <div>48210 Pellman Avenue, Suite 415<br>Woodland Hills, California 90812</div>
  </div>
</section>

</body>
</html>
```